Vertriebsweg.de

The nordische-policenmarkt.de (npm) is an internet portal for the incurance industry in Germany: www.nordische-policenmarkt.de.

We are now planning to start a new brand Vertriebswege.de, which will be integral part of npm, but will have own logo, navigation etc. The main topic of Vertriebswege.de will be the new digital way of communication between insurance companies and insurance brokers (selling companies' products).

The main content of Vertriebswege.de will consist of articles / blog entries and at this moment we would like to concentrate on that part of our new brand.

At the top of the page we will always have a cover story, which will be the latest published article.

Under the cover story the user will find other articles. The articles should have variable widths (1/3, 2/3, 3/3). We will also need some additional elements like newsletter subscription, articles with most clicks etc.

Please use as reference this page:
https://www.kalmer.example/

We really like how it is designed.

Here you will find the current state of our project:

https://relaunch.nordische-policenmarkt.de/vertriebswege

We will also need a logo for Vertriebswege.de, which should include the subtitle: Immer unabhängig, niemals neutral AND powerd by nordische-policenmarkt.de
Updates

Due to the problems with the "Pool" functionality at SketchHarbor we will need more time to verify your projects in our teem - but we are on it.

```html
<!DOCTYPE html>
<html lang="de">
<head>
<meta charset="utf-8">
<title>Vertriebswege.de</title>
<link href="https://fonts.googleapis.com/css2?family=Lato:wght@400;700;900&display=swap" rel="stylesheet">
<style>
:root{
  --red:#e2231a;
  --ink:#1d1d1d;
  --muted:#8a8a8a;
  --page:#cfcfcf;
  --white:#ffffff;
  --line:#dedede;
  --dark:#111111;
}
*{box-sizing:border-box;margin:0;padding:0}
html,body{width:1200px;height:3262px;overflow:hidden}
body{background:var(--page);font-family:'Lato',sans-serif;color:var(--ink);position:relative}
a{color:inherit;text-decoration:none}

.site-header{position:absolute;left:0;top:0;width:1200px;height:116px;background:var(--white)}
.util-links{position:absolute;left:42px;top:49px;font-size:14px;display:flex;gap:31px}
.brand{position:absolute;left:0;width:1200px;top:30px;text-align:center}
.brand-name{font-size:34px;font-weight:900;color:var(--red);display:inline-flex;align-items:center;gap:12px;letter-spacing:-.5px}
.brand-name .mark{width:22px;height:22px;background:var(--dark);display:inline-block}
.brand-sub{font-size:10px;color:var(--muted);margin-top:-2px;padding-left:150px}
.account{position:absolute;right:42px;top:35px;display:flex;align-items:center;gap:16px;font-size:14px}
.round{width:46px;height:46px;border-radius:50%;display:flex;align-items:center;justify-content:center}
.round.user{background:var(--dark)}
.round.menu{background:var(--red)}

.panel{position:absolute;left:42px;width:1116px;background:var(--white);border-radius:8px}
.main-panel{top:142px;height:1959px}
.main-nav{height:64px;border-bottom:1px solid var(--line);position:relative;font-size:15px}
.main-nav .home{position:absolute;left:0;top:0;width:80px;height:64px;border-bottom:3px solid var(--red);display:flex;align-items:center;justify-content:center}
.main-nav .item{position:absolute;top:23px}
.main-nav .search{position:absolute;right:24px;top:19px}

.badge{position:absolute;left:27px;top:27px;background:var(--dark);color:var(--white);font-size:11px;font-weight:700;padding:8px 10px}
.cover{position:absolute;left:25px;top:90px;width:1066px}
.cover .photo{height:417px;position:relative;background:linear-gradient(120deg,#e9e6e1 0%,#b88b63 45%,#5c4636 70%,#d8d8d8 100%)}
.date{display:flex;align-items:center;gap:8px;font-size:14px;color:var(--muted)}
.cover .date{margin-top:32px}
.cover h1{font-size:35px;font-weight:700;margin-top:12px;line-height:42px}
.cover p{font-size:14.5px;line-height:25.5px;margin-top:10px;max-width:1030px}
.btn-read{display:inline-block;margin-top:20px;background:var(--red);color:var(--white);font-size:11px;font-weight:700;padding:9px 14px}
.divider{position:absolute;left:25px;width:1066px;height:1px;background:var(--line)}

.grid{position:absolute;left:24px;display:grid;grid-template-columns:repeat(3,338px);column-gap:26px;grid-auto-rows:562px}
.card .photo{height:338px;position:relative}
.card .date{margin-top:20px;height:20px}
.card h3{font-size:20.5px;font-weight:700;line-height:26.5px;margin-top:15px;max-width:240px}
.card p{font-size:13px;line-height:20.5px;margin-top:6px;max-width:300px}

.p1{background:linear-gradient(135deg,#d9dde2,#8a98a8 50%,#3a3a3a)}
.p2{background:linear-gradient(135deg,#a9c6e6,#d7b09a 55%,#e9eef4)}
.p3{background:linear-gradient(135deg,#3c4650,#eeeeee 45%,#cfcfcf)}
.p4{background:linear-gradient(135deg,#4a6f9a,#e8eef4 50%,#2d89d8)}
.p5{background:linear-gradient(135deg,#5f6468,#c9c6c0 55%,#f0ede8)}
.p6{background:linear-gradient(135deg,#1f1f1f,#e0e0e0 55%,#f4f4f4)}
.p7{background:linear-gradient(180deg,#2c3d58,#dcdcdc 55%,#c23b2b 75%,#ececec)}
.p8{background:linear-gradient(135deg,#f2f2f2,#c4cbd3 50%,#5c6b7d)}
.p9{background:linear-gradient(135deg,#7e9a55,#2b2f38 50%,#e9e5df)}

.newsletter{position:absolute;left:42px;top:2129px;width:1116px;height:134px;background:var(--red);border-radius:8px;color:var(--white)}
.newsletter .icon{position:absolute;left:24px;top:22px}
.newsletter h2{position:absolute;left:130px;top:30px;font-size:20px;font-weight:700;line-height:24px;width:340px}
.newsletter .sub{position:absolute;left:130px;top:84px;font-size:12px}
.newsletter .field{position:absolute;left:734px;top:51px;width:233px;height:33px;background:var(--white);border:1px solid #999;color:var(--muted);font-size:11px;padding:9px 11px}
.newsletter .submit{position:absolute;left:976px;top:51px;width:115px;height:33px;background:var(--dark);font-size:11.5px;font-weight:900;text-align:center;line-height:33px}

.reco-panel{top:2292px;height:665px}
.reco-head{position:absolute;left:24px;top:22px;font-size:19px;font-weight:700}
.reco-more{position:absolute;right:24px;top:24px;font-size:14px;color:var(--red);display:flex;align-items:center;gap:10px}

.site-footer{top:2991px;height:212px}
.foot-brand{position:absolute;left:57px;top:50px}
.foot-brand .brand-name{font-size:30px}
.foot-brand .brand-sub{padding-left:140px;text-align:left}
.copyright{position:absolute;left:55px;top:137px;font-size:14px}
.foot-links{position:absolute;top:54px;font-size:14px;line-height:27.5px}
.foot-rule{position:absolute;left:762px;top:45px;width:1px;height:120px;background:var(--line)}
.social{position:absolute;left:794px;top:86px;display:flex;gap:12px}
.social span{width:42px;height:42px;border-radius:50%;background:var(--dark)}
</style>
</head>
<body>

<header class="site-header">
  <nav class="util-links"><a href="#">Hilfe</a><a href="#">Sitemap</a></nav>
  <div class="brand">
    <div class="brand-name"><span class="mark"></span>Vertriebswege.de</div>
    <div class="brand-sub">nordische-policenmarkt.de</div>
  </div>
  <div class="account">
    <span>Sign In</span>
    <span class="round user"><svg width="22" height="22" viewBox="0 0 22 22"><circle cx="11" cy="7" r="5" fill="#fff"/><path d="M2 21c0-5 4-8 9-8s9 3 9 8z" fill="#fff"/></svg></span>
    <span class="round menu"><svg width="22" height="18" viewBox="0 0 22 18"><rect y="1" width="22" height="2.5" rx="1" fill="#fff"/><rect y="8" width="22" height="2.5" rx="1" fill="#fff"/><rect y="15" width="22" height="2.5" rx="1" fill="#fff"/></svg></span>
  </div>
</header>

<main class="panel main-panel">
  <nav class="main-nav">
    <a class="home" href="#"><svg width="28" height="26" viewBox="0 0 28 26"><path d="M14 1L1 12h4v13h18V12h4z" fill="#e2231a"/></svg></a>
    <a class="item" style="left:123px" href="#">Prozess-Nachrichten</a>
    <a class="item" style="left:324px;top:21px" href="#">MVP-Systeme</a>
    <a class="item" style="left:477px;top:21px" href="#">Veranstaltungen</a>
    <a class="item" style="left:657px" href="#">Studien</a>
    <a class="item" style="left:776px" href="#">Mediadaten</a>
    <a class="item" style="left:916px" href="#">Newsletter</a>
    <svg class="search" width="28" height="28" viewBox="0 0 28 28"><circle cx="12" cy="12" r="9.5" fill="none" stroke="#777" stroke-width="2"/><path d="M19 19l7 7" stroke="#777" stroke-width="2"/></svg>
  </nav>

  <article class="cover">
    <div class="photo" role="img" aria-label="Geschäftsmann am Schreibtisch mit Smartphone, Laptop und Monitor"><span class="badge">Finanzen</span></div>
    <div class="date"><svg width="16" height="16" viewBox="0 0 16 16"><rect x="1" y="2.5" width="14" height="12.5" rx="1.5" fill="none" stroke="#999"/><path d="M1 6h14M4.5 1v3M11.5 1v3" stroke="#999"/></svg>July 24, 2017</div>
    <h1>Fraud Exposures - Is Your Business at Risk?</h1>
    <p>Although fraud has always been a problem, it appears to be getting worse. In 2020, the Federal Consumer Office received more than 2.1 million fraud reports from consumers. Consumers reported losing mtore than $3.3 billion to fraud, a significant increase compared to 2019, when consumers reported losses of $1.8 billion...</p>
    <a class="btn-read" href="#">Read more</a>
  </article>

  <div class="divider" style="top:794px"></div>

  <section class="grid" style="top:837px">
    <article class="card"><div class="photo p1" role="img" aria-label="Berater im Gespräch am Laptop"><span class="badge">Finanzen</span></div><div class="date"><svg width="16" height="16" viewBox="0 0 16 16"><rect x="1" y="2.5" width="14" height="12.5" rx="1.5" fill="none" stroke="#999"/><path d="M1 6h14M4.5 1v3M11.5 1v3" stroke="#999"/></svg>July 24, 2017</div><h3>Führungswechsel in den Chefetagen</h3><p>Der VdV komplettiert seine Führungsmannschaft. Neue Vorstandsvorsitzende bei der Nordwagen Autoversicherung...</p></article>
    <article class="card"><div class="photo p2" role="img" aria-label="Händedruck zweier Geschäftsleute"><span class="badge">Finanzen</span></div><div class="date"><svg width="16" height="16" viewBox="0 0 16 16"><rect x="1" y="2.5" width="14" height="12.5" rx="1.5" fill="none" stroke="#999"/><path d="M1 6h14M4.5 1v3M11.5 1v3" stroke="#999"/></svg>July 24, 2017</div><h3>Führungswechsel in den Chefetagen</h3><p>Der VdV komplettiert seine Führungsmannschaft. Neue Vorstandsvorsitzende bei der Nordwagen Autoversicherung...</p></article>
    <article class="card"><div class="photo p3" role="img" aria-label="Versicherungsdokument mit Stift"><span class="badge">Finanzen</span></div><div class="date"><svg width="16" height="16" viewBox="0 0 16 16"><rect x="1" y="2.5" width="14" height="12.5" rx="1.5" fill="none" stroke="#999"/><path d="M1 6h14M4.5 1v3M11.5 1v3" stroke="#999"/></svg>July 24, 2017</div><h3>Führungswechsel in den Chefetagen</h3><p>Der VdV komplettiert seine Führungsmannschaft. Neue Vorstandsvorsitzende bei der Nordwagen Autoversicherung...</p></article>
    <article class="card"><div class="photo p4" role="img" aria-label="Hand mit Stift auf blauem Vertragsordner"><span class="badge">Finanzen</span></div><div class="date"><svg width="16" height="16" viewBox="0 0 16 16"><rect x="1" y="2.5" width="14" height="12.5" rx="1.5" fill="none" stroke="#999"/><path d="M1 6h14M4.5 1v3M11.5 1v3" stroke="#999"/></svg>July 24, 2017</div><h3>Führungswechsel in den Chefetagen</h3><p>Der VdV komplettiert seine Führungsmannschaft. Neue Vorstandsvorsitzende bei der Nordwagen Autoversicherung...</p></article>
    <article class="card"><div class="photo p5" role="img" aria-label="Vertragsunterzeichnung am Tisch"><span class="badge">Finanzen</span></div><div class="date"><svg width="16" height="16" viewBox="0 0 16 16"><rect x="1" y="2.5" width="14" height="12.5" rx="1.5" fill="none" stroke="#999"/><path d="M1 6h14M4.5 1v3M11.5 1v3" stroke="#999"/></svg>July 24, 2017</div><h3>Führungswechsel in den Chefetagen</h3><p>Der VdV komplettiert seine Führungsmannschaft. Neue Vorstandsvorsitzende bei der Nordwagen Autoversicherung...</p></article>
    <article class="card"><div class="photo p6" role="img" aria-label="Hände über einer Versicherungspolice"><span class="badge">Finanzen</span></div><div class="date"><svg width="16" height="16" viewBox="0 0 16 16"><rect x="1" y="2.5" width="14" height="12.5" rx="1.5" fill="none" stroke="#999"/><path d="M1 6h14M4.5 1v3M11.5 1v3" stroke="#999"/></svg>July 24, 2017</div><h3>Führungswechsel in den Chefetagen</h3><p>Der VdV komplettiert seine Führungsmannschaft. Neue Vorstandsvorsitzende bei der Nordwagen Autoversicherung...</p></article>
  </section>
</main>

<section class="newsletter">
  <svg class="icon" width="84" height="90" viewBox="0 0 84 90"><circle cx="46" cy="38" r="32" fill="none" stroke="#fff" stroke-width="3"/><rect x="30" y="26" width="32" height="24" rx="2" fill="none" stroke="#fff" stroke-width="3" transform="rotate(-30 46 38)"/><path d="M31 30l15 10 15-10" fill="none" stroke="#fff" stroke-width="3" transform="rotate(-30 46 38)"/><path d="M4 66c6-4 10 4 16 0M2 76c6-4 10 4 16 0M8 86c6-4 10 4 16 0" fill="none" stroke="#fff" stroke-width="3"/></svg>
  <h2>Abonnieren Sie unsere wöchentliche Newsletter.</h2>
  <div class="sub">Abonnieren Sie unsere Top-Storys.</div>
  <div class="field">E-Mail Adresse eingeben</div>
  <div class="submit">ABONNIEREN</div>
</section>

<section class="panel reco-panel">
  <h2 class="reco-head">Our recommendations for you</h2>
  <a class="reco-more" href="#">More posts <svg width="22" height="14" viewBox="0 0 22 14"><path d="M0 7h20M14 1l6 6-6 6" fill="none" stroke="#e2231a" stroke-width="2"/></svg></a>
  <div class="divider" style="top:63px;left:24px;width:1068px"></div>
  <div class="grid" style="top:106px">
    <article class="card"><div class="photo p7" role="img" aria-label="Schützende Hände über Haus, Familie und Auto"><span class="badge">Finanzen</span></div><div class="date"><svg width="16" height="16" viewBox="0 0 16 16"><rect x="1" y="2.5" width="14" height="12.5" rx="1.5" fill="none" stroke="#999"/><path d="M1 6h14M4.5 1v3M11.5 1v3" stroke="#999"/></svg>July 24, 2017</div><h3>Führungswechsel in den Chefetagen</h3><p>Der VdV komplettiert seine Führungsmannschaft. Neue Vorstandsvorsitzende bei der Nordwagen Autoversicherung...</p></article>
    <article class="card"><div class="photo p8" role="img" aria-label="Geschäftsmann im Büro mit Tablet"><span class="badge">Finanzen</span></div><div class="date"><svg width="16" height="16" viewBox="0 0 16 16"><rect x="1" y="2.5" width="14" height="12.5" rx="1.5" fill="none" stroke="#999"/><path d="M1 6h14M4.5 1v3M11.5 1v3" stroke="#999"/></svg>July 24, 2017</div><h3>Führungswechsel in den Chefetagen</h3><p>Der VdV komplettiert seine Führungsmannschaft. Neue Vorstandsvorsitzende bei der Nordwagen Autoversicherung...</p></article>
    <article class="card"><div class="photo p9" role="img" aria-label="Beratungsgespräch im Büro"><span class="badge">Finanzen</span></div><div class="date"><svg width="16" height="16" viewBox="0 0 16 16"><rect x="1" y="2.5" width="14" height="12.5" rx="1.5" fill="none" stroke="#999"/><path d="M1 6h14M4.5 1v3M11.5 1v3" stroke="#999"/></svg>July 24, 2017</div><h3>Führungswechsel in den Chefetagen</h3><p>Der VdV komplettiert seine Führungsmannschaft. Neue Vorstandsvorsitzende bei der Nordwagen Autoversicherung...</p></article>
  </div>
</section>

<footer class="panel site-footer">
  <div class="foot-brand">
    <div class="brand-name"><span class="mark"></span>Vertriebswege.de</div>
    <div class="brand-sub">nordische-policenmarkt.de</div>
  </div>
  <div class="copyright">© nordische-policenmarkt.de</div>
  <nav class="foot-links" style="left:502px"><div>AGB</div><div>Datenschutz</div><div>Hilfe</div><div>Impressum</div></nav>
  <nav class="foot-links" style="left:648px"><div>Anfahrt</div><div>Sitemap</div><div>Team</div><div>Mediadaten</div></nav>
  <div class="foot-rule"></div>
  <div class="social" aria-label="Soziale Netzwerke"><span></span><span></span><span></span><span></span><span></span></div>
</footer>

</body>
</html>
```